Tidewell Vitality Autumn Kickoff Quest advertisement design

We need an advertisement for a health, fitness and wellbeing company promoting a new service. The Autumn Kickoff Quest is a 10 week challenge where people choose from 2 program streams - either 1. Fat Loss or 2. Build Lean Muscle. Access to 40 group functional fitness sessions a week, access to exclusive discounts from Brisk Pantry Co. (BPC), discounts on personal training, a targeted gym program, full gym access for the duration of the Challenge and access to Exercise Physiologists and a Sports Dietitian. This is an Tidewell Vitality service co-branded with Brisk Pantry Co.. The final design should be in line with the style guide, be motivating and communicate a point of difference in the fitness industry.

Target Market(s)

men and women ages 30-50yrs, interested in improving their health and lifestyle

Industry/Entity Type

Fitness

Font styles to use
Other font styles liked:
• see style guide

Colors
000000
5c5c5c
9d9d9d
33b8a4
00a990

Requirements
Must have
• professional and exclusive look and feel, motivating tone
Nice to have
• clean design, not too overcrowding, use key pieces of information only and try to stay within the style guide for colour scheme (what is indicated below is the closest pick to our style guide but colour codes are within)
Should not have
• My project should not have any images that cheapen the challenge to look more like a general gym or body sculpting boot camp

```html
<!DOCTYPE html>
<html lang="en">
<head>
<meta charset="utf-8">
<title>Autumn Kickoff Quest</title>
<link rel="stylesheet" href="https://fonts.googleapis.com/css2?family=Open+Sans:wght@300;400;600&display=swap">
<style>
  :root {
    --black: #000000;
    --ink: #0b0d0e;
    --charcoal: #1c1f21;
    --grey-dark: #5c5c5c;
    --grey: #9d9d9d;
    --teal-light: #33b8a4;
    --teal: #00a990;
    --white: #ffffff;
  }
  html, body {
    margin: 0;
    padding: 0;
    overflow: hidden;
    background: var(--black);
  }
  .poster {
    position: relative;
    width: 849px;
    height: 1200px;
    overflow: hidden;
    background: var(--ink);
    font-family: "Open Sans", Arial, sans-serif;
    color: var(--white);
  }
  .top-band {
    position: absolute;
    left: 0; top: 0;
    width: 849px; height: 58px;
    background: var(--teal-light);
    display: flex;
    align-items: center;
    justify-content: center;
    font-size: 19px;
    letter-spacing: 4px;
    color: var(--ink);
    font-weight: 400;
  }
  .hero-photo {
    position: absolute;
    left: 0; top: 58px;
    width: 849px; height: 760px;
    background:
      radial-gradient(ellipse 260px 360px at 640px 360px, #6d7274 0%, #3a3e40 45%, rgba(20,22,24,0) 100%),
      linear-gradient(180deg, #2a2e30 0%, #15181a 70%, var(--ink) 100%);
  }
  .title {
    position: absolute;
    left: 62px; top: 110px;
    margin: 0;
    width: 460px;
    font-size: 50px;
    line-height: 60px;
    font-weight: 400;
    color: var(--teal-light);
  }
  .streams-intro {
    position: absolute;
    left: 62px; top: 388px;
    margin: 0;
    font-size: 27px;
    font-weight: 300;
  }
  .streams {
    position: absolute;
    left: 62px; top: 430px;
    margin: 0; padding: 0;
    list-style: none;
  }
  .streams li {
    display: flex;
    align-items: center;
    gap: 14px;
    font-size: 30px;
    line-height: 40px;
    color: var(--teal-light);
  }
  .features {
    position: absolute;
    left: 108px; top: 525px;
    margin: 0; padding: 0;
    list-style: none;
  }
  .features li {
    position: relative;
    padding-left: 24px;
    font-size: 16px;
    line-height: 24px;
    font-weight: 400;
  }
  .features li::before {
    content: "";
    position: absolute;
    left: 0; top: 8px;
    width: 9px; height: 9px;
    background: var(--teal-light);
  }
  .brand-host {
    position: absolute;
    left: 62px; top: 848px;
    font-size: 44px;
    font-weight: 400;
    color: var(--white);
    letter-spacing: 1px;
  }
  .brand-partner {
    position: absolute;
    left: 656px; top: 828px;
    width: 140px; height: 104px;
    border: 2px solid var(--grey);
    background: var(--charcoal);
    display: flex;
    align-items: center;
    justify-content: center;
    text-align: center;
    font-size: 17px;
    font-weight: 400;
    color: var(--white);
  }
  .divider {
    position: absolute;
    left: 62px; top: 958px;
    width: 725px; height: 2px;
    background: var(--teal-light);
  }
  .joint-venture {
    position: absolute;
    left: 0; top: 990px;
    width: 849px;
    margin: 0;
    text-align: center;
    font-size: 19px;
    color: var(--teal-light);
  }
  .copyright {
    position: absolute;
    left: 0; top: 1030px;
    width: 849px;
    margin: 0;
    text-align: center;
    font-size: 11px;
    color: var(--grey);
  }
</style>
</head>
<body>
<div class="poster">
  <div class="hero-photo" role="img" aria-label="Grainy dark photograph of an athlete doing a pull-up on a gym bar"></div>

  <header class="top-band">10 WEEK AUTUMN KICKOFF QUEST</header>

  <h1 class="title">The Autumn Kickoff Quest</h1>

  <p class="streams-intro">2 program streams to choose from:</p>
  <ul class="streams">
    <li>
      <svg width="28" height="24" viewBox="0 0 28 24" aria-hidden="true">
        <rect x="1" y="1" width="26" height="22" fill="none" stroke="#33b8a4" stroke-width="1.5"/>
        <polyline points="3,13 9,13 11,7 14,18 17,4 19,13 25,13" fill="none" stroke="#33b8a4" stroke-width="2"/>
      </svg>
      Fat Loss or
    </li>
    <li>
      <svg width="28" height="24" viewBox="0 0 28 24" aria-hidden="true">
        <rect x="1" y="1" width="26" height="22" fill="none" stroke="#33b8a4" stroke-width="1.5"/>
        <polyline points="3,13 9,13 11,7 14,18 17,4 19,13 25,13" fill="none" stroke="#33b8a4" stroke-width="2"/>
      </svg>
      Build Lean Muscle.
    </li>
  </ul>

  <ul class="features">
    <li>A targeted 10 week gym program</li>
    <li>Access to exclusive discounts from Brisk Pantry Co. (BPC)</li>
    <li>Discounts on personal training</li>
    <li>Full gym access for the duration of the Challenge and</li>
    <li>Access to Exercise Physiologists and a Sports Dietitian</li>
    <li>Access to 40 group functional fitness sessions a week</li>
    <li>Program cost $500.00 or $100.00 direct fortnightly debt</li>
    <li>Commencing from Monday 1<sup>st</sup> October</li>
    <li>Sports Psychology Seminars</li>
  </ul>

  <div class="brand-host">Tidewell Vitality</div>
  <div class="brand-partner">Brisk Pantry Co.</div>

  <div class="divider"></div>
  <p class="joint-venture">A joint venture of Tidewell Vitality and Brisk Pantry Co.</p>
  <p class="copyright">©2015 Tidewell Vitality. All Rights Reserved</p>
</div>
</body>
</html>
```